Varn Medical needs bold attention catching website for healthcare professionals(target)

I need a hero page as well as a products and about page for a website of mine. I specialize in orthopedic instruments . Specifically bone drills and saws. This whole company was founded to bring superb quality highly discounted medical instruments. Specifically bone drills, bone saws, k-wires and pins. Two main points should be cost savings and superior quality.

Target Market(s)

healthcare professionals Surgeons and hospital material managers

Number of Pages Required

3 page

Font styles to use
Serif

Colors

Designer to choose colors to be used in the design.

Requirements
Must have
• colors should match logo design

```html
<!DOCTYPE html>
<html lang="en">
<head>
<meta charset="utf-8">
<title>Varn Medical — Orthopedic Instruments</title>
<link href="https://fonts.googleapis.com/css2?family=Merriweather:wght@400;700;900&family=Open+Sans:ital,wght@0,400;0,600;1,400&display=swap" rel="stylesheet">
<style>
:root{
  --orange:#ef7d22;
  --orange-dark:#d96a12;
  --ink:#141414;
  --text:#555;
  --grey-bg:#eceef0;
  --line:#e3e3e3;
  --white:#fff;
}
*{box-sizing:border-box;margin:0;padding:0}
html,body{width:1200px;height:4127px;overflow:hidden}
body{position:relative;background:var(--white);font-family:'Merriweather',Georgia,serif;color:var(--ink)}
.abs{position:absolute}
.center{left:0;width:1200px;text-align:center}

/* header */
.brand{font-family:'Merriweather',Georgia,serif;font-weight:700;color:var(--ink);letter-spacing:.5px;display:flex;align-items:center;gap:10px}
.site-brand{left:144px;top:44px;font-size:30px}
.tollfree{left:582px;top:42px;display:flex;align-items:center;gap:12px}
.tollfree .ic{width:34px;height:34px;border-radius:50%;background:var(--orange);display:flex;align-items:center;justify-content:center}
.tollfree small{display:block;font-size:13px;color:#333}
.tollfree strong{font-size:22px;font-weight:400;color:#222}
.search{left:820px;top:51px;width:236px;height:31px;border:1px solid #ccc;border-radius:16px;font-family:'Open Sans',sans-serif;font-size:11px;color:#999;padding:7px 16px}
.search svg{position:absolute;right:10px;top:7px}
.nav{left:0;top:130px;width:1200px;height:48px;background:var(--ink)}
.nav a{position:absolute;top:15px;font-size:15px;color:#fff;text-decoration:none;font-weight:700;letter-spacing:.2px}
.nav a.active{color:var(--orange)}
.nav a.active::after{content:"";position:absolute;left:50%;top:29px;width:2px;height:12px;background:var(--orange)}

/* hero */
.hero-art{left:0;top:178px;width:1200px;height:632px;background:
  linear-gradient(115deg,#dfe4ea 0%,#f6f7f9 30%,#ffffff 50%,#f6f7f9 70%,#dfe4ea 100%)}
.hero-art .wing{position:absolute;top:0;width:260px;height:560px}
.hero-brand{top:320px;justify-content:center;font-size:26px}
.hero-title{top:398px;font-size:74px;font-weight:900}
.hero-sub{top:488px;font-size:38px;color:var(--orange);font-weight:400}
.hero-sub2{top:528px;font-size:48px;font-weight:700}
.btn-fill{background:var(--orange);color:#fff;font-size:14px;font-weight:700;text-align:center;border-radius:3px}
.hero-btn{left:535px;top:610px;width:130px;height:38px;line-height:38px;box-shadow:0 4px 8px rgba(0,0,0,.15)}
.dots{display:flex;gap:10px;justify-content:center;align-items:center}
.dots i{width:11px;height:11px;border-radius:50%;background:var(--ink);display:block}
.dots i.on{width:20px;height:20px;border:2px solid var(--ink);background:radial-gradient(var(--ink) 45%,#fff 50%)}

/* section headings */
.h-sec{font-size:38px;font-weight:700}
.divider{left:525px;width:150px;height:16px}
.lead{left:160px;width:880px;text-align:center;font-family:'Open Sans',sans-serif;font-size:14.5px;line-height:32px;color:var(--text)}

/* feature cards */
.feature{width:443px;height:303px;background:#fff;box-shadow:0 3px 10px rgba(0,0,0,.12)}
.feature .top{position:absolute;left:0;top:0;width:100%;height:225px;padding:34px 28px}
.feature.orange .top{background:var(--orange)}
.feature.dark .top{background:var(--ink)}
.feature h3{position:relative;z-index:2;font-size:22px;font-weight:700;color:#fff;letter-spacing:2px;white-space:nowrap}
.feature hr{border:0;width:60px;height:3px;background:#fff;margin:14px 0 20px}
.feature p{position:relative;z-index:2;font-size:14px;line-height:26.5px;color:#fff;width:250px}
.feature .art{position:absolute;right:18px;top:70px;width:110px;height:220px;border-radius:6px;z-index:1}
.btn-line{position:absolute;border:2px solid var(--ink);font-size:13px;font-weight:700;color:var(--ink);text-align:center;border-radius:3px;background:#fff}
.feature .btn-line{left:27px;top:249px;width:115px;height:34px;line-height:30px}

/* products */
.products-bg{left:0;top:1538px;width:1200px;height:817px;background:linear-gradient(180deg,#f0f1f3,#e6e8eb)}
.product{width:282px;height:433px;background:#fff;border-radius:8px;box-shadow:0 2px 8px rgba(0,0,0,.1);text-align:center}
.product .photo{position:absolute;left:6px;top:6px;width:270px;height:193px;border-radius:6px 6px 0 0}
.product h3{position:absolute;left:0;width:100%;top:224px;font-size:23px;font-weight:700}
.product p{position:absolute;left:22px;width:238px;top:262px;font-size:13.5px;line-height:24px;color:var(--text)}
.product .btn-line{left:83px;top:373px;width:116px;height:33px;line-height:29px}

/* blogs */
.blog-main{left:144px;top:2560px;width:428px;height:365px;box-shadow:0 2px 8px rgba(0,0,0,.12)}
.blog-main .photo{position:absolute;inset:0;background:linear-gradient(160deg,#c9b7a5,#9fb3c7 55%,#4d6a86)}
.blog-main .overlay{position:absolute;left:77px;top:195px;width:351px;height:170px;background:rgba(17,27,40,.92);padding:20px 22px;color:#fff}
.blog-main h4{font-size:18px;line-height:26px;font-weight:700}
.meta{font-family:'Open Sans',sans-serif;font-style:italic;font-size:12.5px;color:var(--orange);display:flex;align-items:center;gap:8px}
.meta .sep{width:1px;height:16px;background:var(--orange);margin:0 10px}
.blog-main .meta{margin:12px 0 10px}
.blog-main p{font-size:13px;line-height:21px}
.blog-side{left:604px;width:452px;height:170px;border:1px solid var(--line);background:#fff}
.blog-side .photo{position:absolute;left:0;top:0;width:189px;height:168px}
.blog-side .body{position:absolute;left:212px;top:16px;width:225px}
.blog-side h4{font-size:17px;font-weight:400;color:#333}
.blog-side .meta{margin:14px 0 12px;font-size:12px}
.blog-side p{font-size:13px;line-height:21px;color:#333}

/* testimonials */
.clients{left:0;top:3036px;width:1200px;height:600px;background:var(--orange)}
.clients-title{top:3100px;color:#fff;font-size:36px;font-weight:700}
.quote{width:300px;top:3237px;display:flex;gap:20px}
.avatar{width:68px;height:68px;border-radius:50%;background:linear-gradient(#f4d9c4,#c98e66);border:3px solid #fff;flex:none}
.quote .txt{font-family:'Open Sans',sans-serif;font-style:italic;color:#fff;font-size:12.5px;line-height:22.5px}
.quote .txt b{font-weight:700;font-style:normal;margin-right:6px}
.quote .who{margin-top:14px;font-size:13px}
.stars{margin-top:10px;font-style:normal;letter-spacing:4px;font-size:17px}
.dots.light i{background:#fff}
.dots.light i.on{border-color:#fff;background:radial-gradient(#fff 40%,var(--orange) 45%)}

/* footer */
.footer{left:0;top:3660px;width:1200px;height:467px;background:var(--ink)}
.footer-head{font-size:18px;font-weight:700;color:#fff}
.footer-brand{left:144px;top:3668px;color:#fff;font-size:28px}
.footer-about{left:144px;top:3746px;width:190px;color:#fff;font-size:13.5px;line-height:24px}
.news-text{left:375px;top:3694px;width:280px;color:#fff;font-size:13.5px;line-height:22px}
.email-input{left:375px;top:3745px;width:274px;height:37px;background:#fff;border-radius:19px;font-family:'Open Sans',sans-serif;font-size:11px;color:#666;padding:10px 16px}
.subscribe{left:375px;top:3800px;width:138px;height:35px;line-height:35px;border-radius:18px}
.contact-row{left:702px;display:flex;gap:16px}
.contact-row svg{flex:none;margin-top:4px}
.contact-row p{color:#fff;font-size:13.5px;line-height:21px}
.quick{left:945px;top:3682px;list-style:none}
.quick li{color:#fff;font-size:13.5px;line-height:27.2px}
.bottom-line{left:0;top:3952px;width:1200px;height:1px;background:#2c2c2c}
.copyright{top:4000px;color:#fff;font-size:13.5px}
.social{left:541px;top:4050px;display:flex;gap:6px}
.social i{display:block;width:28px;height:28px;border:1.5px solid #fff;border-radius:50%}
</style>
</head>
<body>

<!-- header -->
<div class="abs brand site-brand">Varn Medical</div>
<div class="abs tollfree">
  <div class="ic"><svg width="18" height="18" viewBox="0 0 24 24"><path fill="#fff" d="M6.6 10.8a15 15 0 0 0 6.6 6.6l2.2-2.2c.3-.3.7-.4 1-.2 1.1.4 2.3.6 3.6.6.6 0 1 .4 1 1V20c0 .6-.4 1-1 1A17 17 0 0 1 3 4c0-.6.4-1 1-1h3.5c.6 0 1 .4 1 1 0 1.3.2 2.5.6 3.6.1.3 0 .7-.2 1z"/></svg></div>
  <div><small>Toll free :</small><strong>808.5550.1470</strong></div>
</div>
<div class="abs search">Search here<svg width="16" height="16" viewBox="0 0 24 24"><circle cx="10" cy="10" r="7" fill="none" stroke="#888" stroke-width="2.5"/><path d="M15 15l6 6" stroke="#888" stroke-width="2.5"/></svg></div>

<nav class="abs nav">
  <a class="active" style="left:165px">HOME</a>
  <a style="left:252px">ABOUT US</a>
  <a style="left:373px">MEDICAL INSTRUMENTS</a>
  <a style="left:610px">PRODUCTS</a>
  <a style="left:735px">NEWS</a>
  <a style="left:822px">CAREERS</a>
  <a style="left:933px">CONTACT US</a>
</nav>

<!-- hero -->
<div class="abs hero-art" role="img" aria-label="Hero backdrop: orange and grey folded geometric panels with slim steel k-wires standing upright">
  <div class="wing" style="left:0;background:linear-gradient(120deg,#f39a4d 0%,#f0b17a 30%,#c9d3dd 55%,transparent 80%)"></div>
  <div class="wing" style="right:0;background:linear-gradient(240deg,#f39a4d 0%,#f0b17a 30%,#c9d3dd 55%,transparent 80%)"></div>
</div>
<div class="abs center brand hero-brand">Varn Medical</div>
<h1 class="abs center hero-title">Varn Medical</h1>
<div class="abs center hero-sub">Ready for cost</div>
<div class="abs center hero-sub2">savings up to 60%</div>
<div class="abs btn-fill hero-btn">READ MORE</div>
<div class="abs center dots" style="top:724px"><i class="on"></i><i></i><i></i><i></i></div>
<svg class="abs" style="left:0;top:690px" width="1200" height="130" viewBox="0 0 1200 130">
  <path d="M0 14 Q620 190 1200 26 L1200 130 L0 130Z" fill="var(--orange)"/>
  <path d="M0 24 Q620 205 1200 40 L1200 130 L0 130Z" fill="#fff"/>
</svg>

<!-- welcome -->
<h2 class="abs center h-sec" style="top:880px">Welcome to Varn Medical</h2>
<svg class="abs divider" style="top:945px" viewBox="0 0 150 16"><polyline points="0,8 68,8 71,2 75,14 79,8 150,8" fill="none" stroke="var(--orange)" stroke-width="1.6"/></svg>
<p class="abs lead" style="top:978px">Sed ut perspiciatis unde omnis iste natus error sit voluptatem accusantium doloremque laudantium, totam rem aperiam, eaque ipsa quae ab illo inventore veritatis et quasi architecto beatae vitae dicta sunt explicabo. Nemo enim ipsam voluptatem quia voluptas sit aspernatur aut odit aut fugit, sed quia consequuntur magni dolores eos qui ratione voluptatem</p>

<div class="abs feature orange" style="left:143px;top:1121px">
  <div class="top">
    <h3>COST SAVINGS</h3><hr>
    <p>Varn Medical cost savings of up to 50%-60% to its customers. Sed ut perspiciatis unde omnis iste natus error sit voluptatem</p>
  </div>
  <div class="art" role="img" aria-label="Illustration of a cordless bone drill" style="background:linear-gradient(160deg,rgba(0,0,0,0),rgba(20,20,20,.55))"></div>
  <div class="btn-line">READ MORE</div>
</div>
<div class="abs feature dark" style="left:613px;top:1121px">
  <div class="top">
    <h3>SUPERIOR QUALITY</h3><hr>
    <p>Sed ut perspiciatis unde omnis iste natus voluptatem accusantium doloremque laudantium, totam rem aperiam, eaque ipsa quae ab illo</p>
  </div>
  <div class="art" role="img" aria-label="Illustration of a surgical bone saw" style="background:linear-gradient(160deg,#9a9a9a,#5f5f5f 60%,rgba(255,255,255,0))"></div>
  <div class="btn-line">READ MORE</div>
</div>

<!-- products -->
<div class="abs products-bg" role="img" aria-label="Faded operating theatre background"></div>
<svg class="abs" style="left:0;top:1525px" width="1200" height="120" viewBox="0 0 1200 120">
  <path d="M0 0 L1200 0 L1200 110 Q700 -20 0 100Z" fill="#fff"/>
  <path d="M0 100 Q700 -20 1200 110" fill="none" stroke="var(--ink)" stroke-width="9"/>
</svg>
<h2 class="abs center h-sec" style="top:1624px">OUR PRODUCTS</h2>
<svg class="abs divider" style="top:1690px" viewBox="0 0 150 16"><polyline points="0,8 68,8 71,2 75,14 79,8 150,8" fill="none" stroke="var(--orange)" stroke-width="1.6"/></svg>

<div class="abs product" style="left:143px;top:1759px">
  <div class="photo" role="img" aria-label="Photo of a surgeon operating a bone drill" style="background:linear-gradient(135deg,#6b6f74,#2a2c30 60%,#8a7563)"></div>
  <h3>Bone Drills</h3>
  <p>Sed ut perspiciatis unde omnis iste natus error sit voluptatem accustium doloremque laudantium, totam rem aperiam, eaque ipsa quae</p>
  <div class="btn-line">READ MORE</div>
</div>
<div class="abs product" style="left:458px;top:1759px">
  <div class="photo" role="img" aria-label="Photo of bone saw blades on a sterile cloth" style="background:linear-gradient(135deg,#e8e8e8,#a9a9a9 55%,#3d3d3d)"></div>
  <h3>Bone Saws</h3>
  <p>Sed ut perspiciatis unde omnis iste natus error sit voluptatem accustium doloremque laudantium, totam rem aperiam, eaque ipsa quae</p>
  <div class="btn-line">READ MORE</div>
</div>
<div class="abs product" style="left:774px;top:1759px">
  <div class="photo" role="img" aria-label="Photo of k-wires and pins against orange and grey panels" style="background:linear-gradient(120deg,#f39a4d,#e9eef2 45%,#c8d1da 70%,#f39a4d)"></div>
  <h3>K-wires And Pins</h3>
  <p>Sed ut perspiciatis unde omnis iste natus error sit voluptatem accustium doloremque laudantium, totam rem aperiam, eaque ipsa quae</p>
  <div class="btn-line">READ MORE</div>
</div>
<svg class="abs" style="left:0;top:2240px" width="1200" height="130" viewBox="0 0 1200 130">
  <path d="M0 22 Q560 190 1200 10 L1200 130 L0 130Z" fill="var(--orange)"/>
  <path d="M0 32 Q560 205 1200 24 L1200 130 L0 130Z" fill="#fff"/>
</svg>

<!-- blogs -->
<h2 class="abs center h-sec" style="top:2422px">LATEST BLOGS</h2>
<svg class="abs divider" style="top:2488px" viewBox="0 0 150 16"><polyline points="0,8 68,8 71,2 75,14 79,8 150,8" fill="none" stroke="var(--orange)" stroke-width="1.6"/></svg>

<div class="abs blog-main">
  <div class="photo" role="img" aria-label="Photo of gloved hands holding a surgical instrument in a clinic"></div>
  <div class="overlay">
    <h4>Nemo enim ipsam voluptatem quia voluptas</h4>
    <div class="meta"><span>Jan 25, 2019</span><span class="sep"></span><span>2 comments</span></div>
    <p>Sed ut perspiciatis unde omnis iste natus error sit vuptatem accusantium doloremque</p>
  </div>
</div>
<div class="abs blog-side" style="top:2560px">
  <div class="photo" role="img" aria-label="Photo of surgeons' hands with instruments" style="background:linear-gradient(135deg,#d8dde2,#4a525a 60%,#1f2328)"></div>
  <div class="body">
    <h4>Nemo enim ipsam volupta</h4>
    <div class="meta"><span>Jan 25, 2019</span><span class="sep"></span><span>2 comments</span></div>
    <p>Sed ut perspiciatis unde omnis iste natus error sit vuptatem aum doloremque</p>
  </div>
</div>
<div class="abs blog-side" style="top:2752px">
  <div class="photo" role="img" aria-label="Photo of an operation under theatre lights" style="background:linear-gradient(135deg,#1f8a9a,#0f4d5c 60%,#caa48a)"></div>
  <div class="body">
    <h4>Nemo enim ipsam volupta</h4>
    <div class="meta"><span>Jan 25, 2019</span><span class="sep"></span><span>2 comments</span></div>
    <p>Sed ut perspiciatis unde omnis iste natus error sit vuptatem aum doloremque</p>
  </div>
</div>

<!-- testimonials -->
<div class="abs clients"></div>
<h2 class="abs center clients-title">WHAT OUR CLIENTS SAY</h2>
<svg class="abs divider" style="top:3158px" viewBox="0 0 150 16"><polyline points="0,8 68,8 71,2 75,14 79,8 150,8" fill="none" stroke="#fff" stroke-width="1.6"/></svg>

<div class="abs quote" style="left:144px">
  <div class="avatar" role="img" aria-label="Client portrait"></div>
  <div class="txt"><b>“</b>At vero eos et accusamus et iustodio dignissimos ducimus qui blanditiipraesent ium volutum deleniti atque crupquos<div class="who">Daniel Morrow</div><div class="stars">★★★★☆</div></div>
</div>
<div class="abs quote" style="left:453px">
  <div class="avatar" role="img" aria-label="Client portrait"></div>
  <div class="txt"><b>“</b>At vero eos et accusamus et iustodio dignissimos ducimus qui blanditiipraesent ium volutum deleniti atque crupquos<div class="who">Daniel Morrow</div><div class="stars">★★★★☆</div></div>
</div>
<div class="abs quote" style="left:769px">
  <div class="avatar" role="img" aria-label="Client portrait"></div>
  <div class="txt"><b>“</b>At vero eos et accusamus et iustodio dignissimos ducimus qui blanditiipraesent ium volutum deleniti atque crupquos<div class="who">Daniel Morrow</div><div class="stars">★★★★☆</div></div>
</div>
<div class="abs center dots light" style="top:3448px"><i class="on" style="width:17px;height:17px"></i><i style="width:9px;height:9px"></i><i style="width:9px;height:9px"></i></div>

<!-- footer -->
<svg class="abs" style="left:0;top:3500px" width="1200" height="170" viewBox="0 0 1200 170">
  <path d="M0 110 Q650 -30 1200 20 L1200 38 Q650 -10 0 128Z" fill="#fff"/>
  <path d="M0 128 Q650 -10 1200 38 L1200 170 L0 170Z" fill="var(--ink)"/>
</svg>
<div class="abs footer"></div>
<div class="abs brand footer-brand">Varn Medical</div>
<p class="abs footer-about">Sed ut perspiciatis unde omnis iste natus voluptatem accusantium doloremque laudantium, totam rem aperiam, eaque ipsa quae ab illo inventore veritatis</p>

<h5 class="abs footer-head" style="left:375px;top:3638px">SIGN UP FOR NEWSLETTER</h5>
<p class="abs news-text">excepteur sint occaecat cupidatat non proident, sunt in culpa qui officia deserunt</p>
<div class="abs email-input">Enter email</div>
<div class="abs btn-fill subscribe">SUBSCRIBE</div>

<h5 class="abs footer-head" style="left:702px;top:3640px">CONTACT US</h5>
<div class="abs contact-row" style="top:3696px">
  <svg width="16" height="20" viewBox="0 0 16 20"><path d="M8 0a7 7 0 0 0-7 7c0 5 7 13 7 13s7-8 7-13a7 7 0 0 0-7-7zm0 10a3 3 0 1 1 0-6 3 3 0 0 1 0 6z" fill="#fff"/></svg>
  <p>Varn Medical<br>PO Box 412<br>Harlow Creek, RI 02917</p>
</div>
<div class="abs contact-row" style="top:3776px">
  <svg width="16" height="16" viewBox="0 0 24 24"><path fill="#fff" d="M6.6 10.8a15 15 0 0 0 6.6 6.6l2.2-2.2c.3-.3.7-.4 1-.2 1.1.4 2.3.6 3.6.6.6 0 1 .4 1 1V20c0 .6-.4 1-1 1A17 17 0 0 1 3 4c0-.6.4-1 1-1h3.5c.6 0 1 .4 1 1 0 1.3.2 2.5.6 3.6.1.3 0 .7-.2 1z"/></svg>
  <p>Phone:<br>808-5550-2291</p>
</div>
<div class="abs contact-row" style="top:3828px">
  <svg width="17" height="13" viewBox="0 0 17 13"><rect width="17" height="13" rx="1" fill="#fff"/><path d="M0 1l8.5 6L17 1" fill="none" stroke="var(--ink)" stroke-width="1.5"/></svg>
  <p>Email:<br>info@varnmedical.com</p>
</div>

<h5 class="abs footer-head" style="left:942px;top:3640px">QUICK LINKS</h5>
<ul class="abs quick">
  <li>Home</li><li>About Us</li><li>Medical Instruments</li><li>Products</li><li>News</li><li>Careers</li><li>Contact Us</li>
</ul>

<div class="abs bottom-line"></div>
<p class="abs center copyright">Varn Medical © 2019 All Rights Reserved | Privacy Policy | Terms and Conditions</p>
<div class="abs social" aria-label="Social links"><i></i><i></i><i></i><i></i></div>

</body>
</html>
```